Design the app for the next NestLoop

We need a cutting edge, super UX-intuitive, design for a global parking app called Vamo.
- Homescreen and website have been finalised already (see attached pdf)
- Wireframed screens for the concepts we need have been provided in the attached pdf
- We need some really nice icons for parking space types, etc
- Needs to be very, very intuitive to use and navigate.
References: NestLoop app & Zolt app, for their simplicity of use
Updates
Project Deadline Extended
Reason: A few designers have requested that we extend this deadline. So here you go.
Industry/Entity Type
Parking
Look and feel
Each slider illustrates characteristics of the customer's brand and the style your logo design should communicate.

```html
<!DOCTYPE html>
<html lang="en">
<head>
<meta charset="utf-8">
<title>Vamo – Home</title>
<link rel="stylesheet" href="https://fonts.googleapis.com/css2?family=Lato:wght@300;400&display=swap">
<style>
  :root {
    --bg-dark: #0f0f0f;
    --bg-mid: #2a2a2a;
    --text-light: #ffffff;
    --text-soft: #f2f2f2;
    --brand-red: #b0151f;
    --brand-red-deep: #a30f1a;
  }
  * { margin: 0; padding: 0; box-sizing: border-box; }
  html, body { width: 675px; height: 1200px; overflow: hidden; background: var(--bg-dark); }
  .home-screen {
    position: relative;
    width: 675px;
    height: 1200px;
    overflow: hidden;
    font-family: "Lato", sans-serif;
    color: var(--text-light);
  }
  .backdrop {
    position: absolute;
    inset: 0;
    background:
      radial-gradient(ellipse at 62% 45%, #3a3a3a 0%, rgba(40,40,40,0.6) 35%, transparent 70%),
      linear-gradient(170deg, var(--bg-mid) 0%, #1a1a1a 30%, #222 60%, var(--bg-dark) 100%);
  }
  .brand {
    position: absolute;
    top: 186px;
    left: 0;
    width: 100%;
    text-align: center;
  }
  .brand-square {
    display: block;
    width: 160px;
    height: 160px;
    margin: 0 auto;
    background: var(--text-light);
    border-radius: 10px;
  }
  .brand-name {
    margin-top: 22px;
    font-weight: 300;
    font-size: 44px;
    line-height: 1;
    letter-spacing: 16px;
    padding-left: 16px;
  }
  .tagline {
    margin-top: 19px;
    font-weight: 400;
    font-size: 19px;
    color: var(--text-soft);
  }
  .intro {
    position: absolute;
    top: 518px;
    left: 50px;
    width: 575px;
    text-align: center;
    font-weight: 300;
    font-size: 26px;
    line-height: 34.6px;
    letter-spacing: -1.1px;
    color: var(--text-soft);
  }
  .actions {
    position: absolute;
    top: 824px;
    left: 66px;
    width: 544px;
  }
  .action-button {
    display: flex;
    align-items: center;
    justify-content: center;
    height: 108px;
    margin-bottom: 22px;
    background: linear-gradient(90deg, var(--brand-red) 0%, var(--brand-red-deep) 50%, var(--brand-red) 100%);
    color: var(--text-light);
    font-size: 34px;
    font-weight: 400;
    letter-spacing: -1.6px;
    text-decoration: none;
    word-spacing: 3px;
  }
</style>
</head>
<body>
  <main class="home-screen">
    <div class="backdrop" role="img" aria-label="Blurred black-and-white street photo with parking meters and a parking sign"></div>

    <header class="brand">
      <span class="brand-square"></span>
      <h1 class="brand-name">VAMO</h1>
      <p class="tagline">Your private parking space</p>
    </header>

    <p class="intro">Lorem Ipsum is simply dummy text of the printing and typesetting industry. Lorem Ipsum has been the industry's standard dummy text ever since the 1500s, when an unknown printer took a galley of type and scrambled</p>

    <nav class="actions">
      <a class="action-button" href="#">LEASE YOUR PARKING SPACE</a>
      <a class="action-button" href="#">SEARCH&nbsp; FOR&nbsp; PARKING</a>
    </nav>
  </main>
</body>
</html>
```